Linkmesa and Glimtoria advertising

We need Linkmesa and Glimtoria ads. Simple ad with Alaska themed background.
This ad is to introduce our new ZENIRO Internet service.
--Speeds to 500 mpbs
-- Packages start at only $89.99 for speeds to 100mbps
-- Fiber Optic based connection, Not satellite
-- Extreme low latency, consistent speeds
--FREE equipment, FREE Installation, FREE wifi router, First month of service FREE

```html
<!DOCTYPE html>
<html lang="en">
<head>
<meta charset="utf-8">
<title>ZENIRO Internet Service</title>
<link href="https://fonts.googleapis.com/css2?family=Archivo+Black&family=Bebas+Neue&family=Oswald:wght@200&family=Poppins:wght@300;400;600;700&display=swap" rel="stylesheet">
<style>
  :root {
    --navy: #0b1f33;
    --cyan: #18e4ff;
    --sky: #3aa8ff;
    --pink: #f074b6;
    --pink-soft: #dc7ab7;
    --pink-hot: #f15c9a;
    --tab-teal: #0a7a88;
    --ink: #0b1a33;
    --white: #ffffff;
  }
  * { margin: 0; padding: 0; box-sizing: border-box; }
  html, body { width: 1200px; height: 1200px; overflow: hidden; background: var(--navy); }
  .ad {
    position: relative;
    width: 1200px;
    height: 1200px;
    overflow: hidden;
    font-family: "Poppins", sans-serif;
    color: var(--white);
  }
  .scenery {
    position: absolute; inset: 0;
    background:
      radial-gradient(ellipse 280px 420px at 690px 470px, rgba(31,200,180,0.55), transparent 70%),
      linear-gradient(180deg, #0a2336 0%, #0f3a4c 30%, #167a86 52%, #3f9fc0 62%, #6fb9d6 72%, #2f8fb4 80%, #1b5f82 88%, #0b2338 100%);
  }
  .headline { position: absolute; left: 0; top: 0; font-weight: 400; }
  .headline span { position: absolute; display: block; white-space: nowrap; }
  .headline-brand {
    left: 92px; top: 88px;
    font-family: "Archivo Black", sans-serif;
    font-size: 90px; line-height: 90px; letter-spacing: 12px; color: var(--white);
  }
  .headline-main {
    left: 92px; top: 167px;
    font-family: "Bebas Neue", sans-serif;
    font-size: 180px; line-height: 180px; letter-spacing: 2px;
    background: linear-gradient(180deg, var(--cyan), var(--sky));
    -webkit-background-clip: text; background-clip: text; color: transparent;
  }
  .headline-sub {
    left: 92px; top: 318px;
    font-family: "Archivo Black", sans-serif;
    font-size: 114px; line-height: 114px; letter-spacing: -3px; color: var(--white);
  }
  .speed-bar {
    position: absolute; left: 94px; top: 454px; width: 539px; height: 156px;
    border-radius: 20px; overflow: hidden; display: flex;
  }
  .speed-label {
    width: 227px; background: var(--pink); display: flex; align-items: center; justify-content: center;
    font-family: "Bebas Neue", sans-serif; font-size: 56px; color: var(--white);
  }
  .speed-value {
    flex: 1; background: var(--cyan); display: flex; align-items: center; justify-content: center;
    font-family: "Bebas Neue", sans-serif; font-size: 84px; color: #0a0a0a;
  }
  .price-card { position: absolute; left: 707px; top: 102px; width: 415px; height: 320px; }
  .price-card svg { position: absolute; inset: 0; }
  .price-tab {
    position: absolute; top: 16px; left: 0; width: 100%; text-align: center;
    font-family: "Bebas Neue", sans-serif; font-size: 36px; color: var(--ink);
  }
  .price-line {
    position: absolute; top: 95px; width: 100%; text-align: center;
    font-family: "Bebas Neue", sans-serif; font-size: 88px; line-height: 1;
  }
  .price-only { font-family: "Oswald", sans-serif; font-weight: 200; font-size: 78px; color: var(--white); letter-spacing: -2px; }
  .price-amount { color: var(--ink); }
  .price-note {
    position: absolute; top: 198px; width: 100%; text-align: center;
    font-weight: 400; font-size: 25px; letter-spacing: 5px; color: var(--white);
  }
  .price-speed {
    position: absolute; top: 228px; width: 100%; text-align: center;
    font-family: "Archivo Black", sans-serif; font-size: 50px; color: var(--ink);
  }
  .feature { position: absolute; left: 702px; display: flex; align-items: center; gap: 20px; }
  .feature-icon {
    width: 62px; height: 62px; border-radius: 50%; background: var(--cyan);
    display: flex; align-items: center; justify-content: center; flex-shrink: 0;
  }
  .feature-text { font-weight: 700; font-size: 27px; line-height: 1.22; }
  .free { position: absolute; left: 97px; top: 968px; display: flex; align-items: center; gap: 12px; }
  .free-word {
    font-family: "Bebas Neue", sans-serif; font-size: 168px; line-height: 1;
    background: linear-gradient(180deg, var(--pink-hot), #f28ad6);
    -webkit-background-clip: text; background-clip: text; color: transparent;
  }
  .free-list { list-style: none; font-weight: 600; font-size: 23px; line-height: 34px; }
  .free-list li { display: flex; align-items: center; gap: 8px; }
  .brand { position: absolute; left: 700px; top: 976px; display: flex; align-items: center; gap: 45px; }
  .brand-mark {
    width: 100px; height: 53px; background: #1a2a4a;
    display: flex; align-items: center; padding-left: 8px;
    font-weight: 600; font-size: 16px; color: var(--white);
  }
  .brand-name { font-weight: 600; font-size: 36px; color: var(--white); }
  .visit {
    position: absolute; left: 700px; top: 1040px; width: 423px;
    display: flex; align-items: center; gap: 8px;
    font-weight: 700; font-size: 26px; letter-spacing: 3px; color: var(--pink);
  }
  .visit::after { content: ""; flex: 1; height: 2px; background: var(--white); }
  .web { position: absolute; left: 700px; top: 1071px; font-weight: 400; font-size: 34px; white-space: nowrap; }
  .web strong { font-weight: 600; color: var(--cyan); }
</style>
</head>
<body>
<main class="ad">
  <div class="scenery" role="img" aria-label="Alaskan night scene with green northern lights over snowy mountains and a frozen lake"></div>

  <h1 class="headline">
    <span class="headline-brand">ZENIRO</span>
    <span class="headline-main">INTERNET</span>
    <span class="headline-sub">SERVICE</span>
  </h1>

  <div class="speed-bar">
    <div class="speed-label">SPEEDS TO</div>
    <div class="speed-value">500 MPBS</div>
  </div>

  <section class="price-card">
    <svg width="415" height="320" viewBox="0 0 415 320">
      <path d="M0 36 Q0 16 20 16 H395 Q415 16 415 36 V300 Q415 320 395 320 H20 Q0 320 0 300 Z" fill="#dc7ab7"/>
      <path d="M0 36 Q0 16 20 16 H395 Q415 16 415 36 H0 Z" fill="#0a7a88"/>
      <path d="M30 0 H384 Q360 4 350 36 Q340 70 300 70 H115 Q75 70 65 36 Q55 4 30 0 Z" fill="#18e4ff"/>
    </svg>
    <div class="price-tab">PACKAGES START AT</div>
    <div class="price-line"><span class="price-only">ONLY</span> <span class="price-amount">$89.99</span></div>
    <div class="price-note">FOR SPEEDS TO</div>
    <div class="price-speed">100MBPS</div>
  </section>

  <div class="feature" style="top:459px">
    <div class="feature-icon">
      <svg width="34" height="34" viewBox="0 0 34 34" fill="none" stroke="#0b1a33" stroke-width="3" stroke-linecap="round">
        <path d="M8 22 Q17 32 26 22"/><path d="M17 26 V8"/><path d="M11 24 V12"/><path d="M23 24 V12"/>
        <circle cx="17" cy="6" r="2.5" fill="#0b1a33"/><circle cx="11" cy="10" r="2.5" fill="#0b1a33"/><circle cx="23" cy="10" r="2.5" fill="#0b1a33"/>
      </svg>
    </div>
    <p class="feature-text">Fiber Optic based<br>connection, Not satellite</p>
  </div>

  <div class="feature" style="top:548px">
    <div class="feature-icon">
      <svg width="34" height="34" viewBox="0 0 34 34" fill="none" stroke="#0b1a33" stroke-width="3" stroke-linecap="round">
        <rect x="5" y="5" width="24" height="13" rx="2"/><circle cx="17" cy="11.5" r="3" fill="#0b1a33"/>
        <path d="M9 22 V30 M6 27 L9 30 L12 27 M17 22 V30 M14 27 L17 30 L20 27 M25 22 V30 M22 27 L25 30 L28 27"/>
      </svg>
    </div>
    <p class="feature-text">Extreme low latency,<br>consistent speeds</p>
  </div>

  <div class="free">
    <div class="free-word">FREE</div>
    <ul class="free-list">
      <li><svg width="12" height="12" viewBox="0 0 12 12"><circle cx="6" cy="6" r="6" fill="#18e4ff"/><path d="M3.3 6.2 L5.2 8 L8.7 4.2" stroke="#0b1a33" stroke-width="1.6" fill="none"/></svg>Equipment</li>
      <li><svg width="12" height="12" viewBox="0 0 12 12"><circle cx="6" cy="6" r="6" fill="#18e4ff"/><path d="M3.3 6.2 L5.2 8 L8.7 4.2" stroke="#0b1a33" stroke-width="1.6" fill="none"/></svg>Installation</li>
      <li><svg width="12" height="12" viewBox="0 0 12 12"><circle cx="6" cy="6" r="6" fill="#18e4ff"/><path d="M3.3 6.2 L5.2 8 L8.7 4.2" stroke="#0b1a33" stroke-width="1.6" fill="none"/></svg>Wifi router</li>
      <li><svg width="12" height="12" viewBox="0 0 12 12"><circle cx="6" cy="6" r="6" fill="#18e4ff"/><path d="M3.3 6.2 L5.2 8 L8.7 4.2" stroke="#0b1a33" stroke-width="1.6" fill="none"/></svg>First month of service</li>
    </ul>
  </div>

  <div class="brand">
    <div class="brand-mark">ZENIRO</div>
    <div class="brand-name">Northvale Fiber</div>
  </div>
  <div class="visit">VISIT US</div>
  <div class="web">www.<strong>northvalefiber</strong>.com</div>
</main>
</body>
</html>
```